Overview of Elder Abuse Resources Brochure

We need a 2-page brochure that provides a list of resources for elders in tribal communities in the US and those who care for them. We want it to be simple and easy to read, and easy to see the difference between each resource. We would also like eye-catching images or graphics. Please keep the images on the front, and add any photos or graphics that depict Native American elders. We need both of our logos on the first page, in the far-right column. Please refer to the attached image for our brand colors and a font suggestion. Please keep the three columns on each page, but delete the blank pages in the document.

```html
<!DOCTYPE html>
<html lang="en">
<head>
<meta charset="utf-8">
<title>Services for Elders Brochure</title>
<link href="https://fonts.googleapis.com/css2?family=Poppins:ital,wght@0,400;0,500;0,600;0,700;1,400&display=swap" rel="stylesheet">
<style>
  :root{
    --bg:#e2e2e2;
    --paper:#ffffff;
    --clay:#b35a51;
    --teal:#4fa9b3;
    --ink:#121212;
    --soft-gray:#ececec;
    --faint:rgba(255,255,255,.45);
  }
  *{box-sizing:border-box;margin:0;padding:0}
  html,body{width:1200px;height:1200px;overflow:hidden;background:var(--bg);font-family:'Poppins',sans-serif;color:var(--ink)}
  .sheet{position:absolute;left:97px;top:211px;width:1006px;height:778px;background:var(--paper)}

  /* left panel */
  .panel-left{position:absolute;left:0;top:0;width:335px;height:778px}
  .brand-block{height:174px;background:var(--clay);display:flex;align-items:center;justify-content:center;gap:10px}
  .brand-dot{width:14px;height:14px;border-radius:50%;background:#fff}
  .brand-name{color:#fff;font-weight:600;font-size:22px;letter-spacing:.5px}
  .zigzag-band{height:25px;background:repeating-linear-gradient(90deg,var(--clay) 0 12px,var(--teal) 12px 24px);opacity:.85;border-top:3px solid #fff}
  .concerns{padding:14px 22px 0;text-align:center;font-weight:500;font-size:12.6px;line-height:16.5px}
  .concerns p{margin-bottom:14px}
  .help-box{position:absolute;left:23px;top:435px;width:289px;height:320px;border:1.5px solid var(--clay);border-radius:14px;text-align:center}
  .help-label{margin-top:8px;font-size:10.5px}
  .help-main{color:var(--clay);font-weight:700;font-size:14px;line-height:18px;margin-top:4px}
  .resource{font-size:10.8px;line-height:14px;padding:7px 6px}
  .resource.shaded{background:var(--soft-gray);margin:0 6px}
  .resource strong{color:var(--clay);font-weight:700}
  .resource .big{display:block;font-size:15px;line-height:20px;color:var(--clay);font-weight:700}
  .r1{margin-top:76px}

  /* spine */
  .spine{position:absolute;left:611px;top:25px;width:48px;height:240px}
  .spine-name{position:absolute;left:24px;top:0;transform-origin:0 0;transform:rotate(-90deg) translate(-240px,-12px);width:240px;color:var(--clay);font-weight:600;font-size:13px;text-align:center;white-space:nowrap}

  /* right panel */
  .panel-right{position:absolute;left:671px;top:0;width:335px;height:778px}
  .org-mark{position:absolute;top:60px;left:0;width:335px;display:flex;align-items:center;justify-content:center;gap:10px}
  .org-square{width:18px;height:18px;background:var(--teal)}
  .org-name{color:var(--teal);font-weight:600;font-size:21px}
  .zigzag-right{position:absolute;top:219px;left:0;width:335px;height:24px;background:repeating-linear-gradient(90deg,var(--clay) 0 12px,var(--teal) 12px 24px);opacity:.85;border-bottom:2px solid var(--clay)}
  .title{position:absolute;top:252px;left:0;width:335px;text-align:center;font-weight:700;font-size:23.5px;line-height:28px;color:var(--teal)}
  .title .accent{color:var(--clay)}
  .photo{position:absolute;top:351px;height:166px;width:165px}
  .photo.a{left:0;background:linear-gradient(135deg,#8f8f8f,#5a5550 60%,#3a3836)}
  .photo.b{left:170px;background:linear-gradient(135deg,#6b2a20,#c23a3a 45%,#8a1c4a 75%,#2e7a4a)}
  .info{position:absolute;top:522px;left:0;width:335px;height:256px;background:linear-gradient(180deg,var(--teal) 0%,var(--teal) 52%,#9a8d88 78%,var(--clay) 100%);padding:12px 20px 0 40px;color:#fff}
  .info ul{list-style:none}
  .info li{position:relative;font-size:13.6px;line-height:17.5px;margin-bottom:10px}
  .info li svg{position:absolute;left:-17px;top:1px}
  .who{position:absolute;left:0;top:158px;width:335px;height:90px;color:var(--faint);font-style:italic;font-size:16.5px}
  .who span{position:absolute}
</style>
</head>
<body>
<div class="sheet">

  <section class="panel-left">
    <div class="brand-block">
      <span class="brand-dot"></span>
      <span class="brand-name">Elder Justice Circle</span>
    </div>
    <div class="zigzag-band" role="img" aria-label="Decorative zigzag pattern band in clay and teal"></div>
    <div class="concerns">
      <p>Do you have concerns about an Elder, maybe you see that they are not taking care of themselves, or family only comes once a month when the Elder has money?</p>
      <p>Is an Elder telling you that they are not treated with respect or that someone is bothering them?</p>
      <p>These may be signs of Elder abuse, neglect or exploitation.</p>
    </div>
    <div class="help-box">
      <p class="help-label">FOR HELP CONTACT:</p>
      <p class="help-main">Your Tribal Social Services<br>or Elders Department</p>
      <div class="resource shaded r1">The Elder Care Finder for<br>information on Adult Protective Services<span class="big">1-800-555-0142</span></div>
      <div class="resource">If a serious emergency, <strong>call 555</strong></div>
      <div class="resource shaded">For mental health support for yourself<br>or an Elder, <strong>call or text 555-0188</strong></div>
      <div class="resource">Domestic Violence Hotline<br><strong>1.800.555.CARE (2273)</strong></div>
    </div>
  </section>

  <div class="spine"><div class="spine-name">Indigenous Elders Network</div></div>

  <section class="panel-right">
    <div class="org-mark"><span class="org-square"></span><span class="org-name">Indigenous Elders Network</span></div>
    <div class="zigzag-right" role="img" aria-label="Decorative zigzag pattern band in clay and teal"></div>
    <h1 class="title"><span class="accent">SERVICES FOR ELDERS</span><br>&amp; PEOPLE WHO CARE<br>FOR THEM</h1>
    <div class="photo a" role="img" aria-label="Photo of a Native American elder man with long grey hair"></div>
    <div class="photo b" role="img" aria-label="Photo of a Native American elder woman wrapped in a colourful blanket"></div>
    <div class="info">
      <ul>
        <li><svg width="10" height="10" viewBox="0 0 10 10"><path d="M1 5l3 3 5-7" fill="none" stroke="var(--clay)" stroke-width="1.8"/></svg>Are you caring for an Elder or a Grandchild?</li>
        <li><svg width="10" height="10" viewBox="0 0 10 10"><path d="M1 5l3 3 5-7" fill="none" stroke="var(--clay)" stroke-width="1.8"/></svg>Are you an Elder who needs help staying at home?</li>
        <li><svg width="10" height="10" viewBox="0 0 10 10"><path d="M1 5l3 3 5-7" fill="none" stroke="var(--clay)" stroke-width="1.8"/></svg>These programs and information can be a helpful resource.</li>
      </ul>
      <div class="who">
        <span style="left:37px;top:0">MY MOTHER</span>
        <span style="left:185px;top:0">MY FATHER</span>
        <span style="left:107px;top:26px">MY GRANDCHILD</span>
        <span style="left:76px;top:52px">MY SISTER</span>
        <span style="left:229px;top:52px">MYSELF</span>
      </div>
    </div>
  </section>

</div>
</body>
</html>
```